Bramwell Resources Ltd. - Refreshed business card challenge

A revised, refreshed business card design for my oil and gas company using my existing logo. Feel free to be as creative as you like!

Target Market(s)

bankers, lawyers

Industry/Entity Type

Oil And Gas Exploration

Contact Information for Business Card

See the "Must Haves" section

Font styles to use
Serif
Sans Serif

Colors

Designer to choose colors to be used in the design.

Requirements
Must have
• Existing business logo, name, title, email, phone number, business address
• Neil Hadley, CA, CPA
• Vice President Finance & Chief Financial Officer
• nhadley@bramwellresources-mail.com
• office: (587)555-0142
• cell: (403)555-0187
• 1400, 815 4 Street S.W.
• Calgary, AB
• T2P 4K8
Should not have
• Should not be plain and boring.

```html
<!DOCTYPE html>
<html lang="en">
<head>
<meta charset="utf-8">
<title>Bramwell Resources Ltd. – Business Card</title>
<link rel="stylesheet" href="https://fonts.googleapis.com/css2?family=Lato:wght@400;700;900&display=swap">
<style>
  :root {
    --forest: #004a2f;
    --forest-deep: #003a25;
    --forest-soft: #d9e4dd;
    --bark: #5a2e12;
    --paper: #ffffff;
    --ink: #3a3a3a;
    --stage: #4a4a4a;
  }
  * { margin: 0; padding: 0; box-sizing: border-box; }
  html, body { width: 1200px; height: 896px; overflow: hidden; }
  body {
    background: var(--stage);
    font-family: "Lato", sans-serif;
    position: relative;
  }
  .card {
    position: absolute;
    left: 260px;
    width: 680px;
    height: 389px;
    overflow: hidden;
    box-shadow: 0 6px 18px rgba(0,0,0,.35);
  }
  .card-front { top: 40px; background: var(--paper); }
  .card-back { top: 467px; background: var(--forest); }

  .front-art {
    position: absolute; left: 0; top: 0;
    width: 270px; height: 389px;
    background: linear-gradient(180deg, var(--forest) 0%, var(--forest-deep) 100%);
  }
  .front-content {
    position: absolute; left: 300px; top: 60px; right: 30px;
  }
  .wordmark {
    font-weight: 900;
    color: var(--forest);
    font-size: 34px;
    line-height: 1.05;
    letter-spacing: -0.5px;
    white-space: nowrap;
  }
  .holder {
    margin-top: 24px;
    color: var(--bark);
    font-weight: 400;
    font-size: 20px;
    text-transform: uppercase;
    letter-spacing: .5px;
  }
  .role, .address, .contact li {
    color: var(--ink);
    font-size: 15px;
    line-height: 1.35;
  }
  .address { margin-top: 10px; }
  .contact { list-style: none; margin-top: 8px; }
  .contact li { display: flex; align-items: center; gap: 8px; white-space: nowrap; }
  .contact svg { width: 13px; height: 13px; flex: none; fill: var(--forest); }

  .back-art {
    position: absolute; left: 250px; top: 40px;
    width: 180px; height: 230px;
    border-radius: 4px;
    background: linear-gradient(180deg, rgba(217,228,221,.55) 0%, rgba(217,228,221,.2) 100%);
  }
  .back-mark {
    position: absolute; left: 0; right: 0; top: 292px;
    text-align: center;
    font-weight: 900;
    font-size: 36px;
    color: var(--paper);
    letter-spacing: -0.5px;
  }
</style>
</head>
<body>
  <section class="card card-front">
    <div class="front-art" role="img" aria-label="Illustration area: tall conifer tree with smaller trees at its base, in green and brown"></div>
    <div class="front-content">
      <div class="wordmark">Bramwell Resources</div>
      <p class="holder">Neil Hadley, CA, CPA</p>
      <p class="role">Vice President Finance &amp;<br>Chief Financial Officer</p>
      <p class="address">1400, 815 4 Street S.W.<br>Calgary, AB T2P 4K8</p>
      <ul class="contact">
        <li><svg viewBox="0 0 16 16"><path d="M3 1h3l1.5 4-2 1.2a9 9 0 0 0 4.3 4.3L11 8.5l4 1.5v3a2 2 0 0 1-2 2A12 12 0 0 1 1 3a2 2 0 0 1 2-2z"/></svg>(587)555-0142</li>
        <li><svg viewBox="0 0 16 16"><path d="M4 0h8a1 1 0 0 1 1 1v14a1 1 0 0 1-1 1H4a1 1 0 0 1-1-1V1a1 1 0 0 1 1-1zm1 2v10h6V2z"/></svg>(403)555-0187</li>
        <li><svg viewBox="0 0 16 16"><path d="M0 3h16v10H0zm1.5 1.2v.4L8 9l6.5-4.4v-.4z"/></svg>nhadley@bramwellresources-mail.com</li>
      </ul>
    </div>
  </section>

  <section class="card card-back">
    <div class="back-art" role="img" aria-label="Illustration area: white conifer tree above the company name"></div>
    <div class="back-mark">Bramwell Resources</div>
  </section>
</body>
</html>
```